" A nossa empresa trabalha com um vale-refeição digital. Fechamos contratos com restaurantes para que eles possam receber a nossa forma de pagamento (cartãozinho do Grupo da Mesada e QR CODE do celular do usuário). Fechamos, então, contratos com empresas para que elas usem o nosso vale-refeição digital, com os usuários delas podendo pesquisar por prato (cardápio), estilo de comida (a la carte, buffet), estilo de cozinha (italiana, alemã, etc) na região onde trabalham (geolocalização) "

```html
<!DOCTYPE html>
<html lang="pt-BR">
<head>
<meta charset="utf-8">
<title>Grupo da Mesada – Conhecimento de mercado</title>
<link href="https://fonts.googleapis.com/css2?family=Roboto+Condensed:wght@300;400;700&family=Roboto:wght@400;700;900&display=swap" rel="stylesheet">
<style>
  :root{
    --page:#eceae8;
    --red:#c4161c;
    --red-dark:#8e0d12;
    --red-deep:#5e080b;
    --white:#ffffff;
    --ink-soft:#f3d6d7;
  }
  *{box-sizing:border-box;margin:0;padding:0}
  html,body{width:1200px;height:1200px;overflow:hidden;background:var(--page)}
  body{font-family:"Roboto",Arial,sans-serif}
  .spread{position:absolute;left:50px;top:170px;width:1100px;height:860px;background:var(--white);overflow:hidden;box-shadow:0 10px 30px rgba(0,0,0,.15)}

  /* left column */
  .knowledge{position:absolute;left:0;top:0;width:340px;height:860px;
    background:linear-gradient(160deg,#b3141a 0%,#a11016 45%,#7d0b10 100%);color:var(--white);padding:34px 26px}
  .knowledge__title{font-family:"Roboto Condensed",Arial,sans-serif;font-weight:700;font-size:31px;line-height:1.05;text-transform:uppercase}
  .knowledge__title span{font-weight:300}
  .insights{list-style:none;margin-top:64px}
  .insight{display:flex;align-items:center;gap:20px;margin-bottom:54px}
  .insight svg{flex:0 0 64px}
  .insight p{font-size:17px;line-height:1.25}
  .insight b{font-weight:900}
  .knowledge__note{position:absolute;left:26px;right:26px;bottom:30px;font-size:9.5px;line-height:1.35;text-transform:uppercase;color:var(--ink-soft);border-top:1px solid rgba(255,255,255,.5);padding-top:8px}

  /* middle column */
  .lead{position:absolute;left:340px;top:0;width:320px;height:240px;background:var(--white);padding:50px 30px}
  .lead h2{font-family:"Roboto Condensed",Arial,sans-serif;font-weight:400;font-size:27px;line-height:1.15;color:var(--red);text-transform:uppercase;border-left:3px solid var(--red);padding-left:14px}
  .lead h2 b{font-weight:700}
  .photo-service{position:absolute;left:340px;top:240px;width:320px;height:310px;background:linear-gradient(135deg,#6d5a4e,#3a2d27 60%,#8c7a6c)}
  .promise{position:absolute;left:340px;top:550px;width:320px;height:310px;background:var(--white);padding:52px 26px;text-align:center}
  .promise p{font-family:"Roboto Condensed",Arial,sans-serif;font-size:22px;line-height:1.3;color:var(--red);text-transform:uppercase}
  .promise b{font-weight:700}

  /* right column */
  .photo-client{position:absolute;left:660px;top:0;width:440px;height:860px;background:linear-gradient(180deg,#d9cbc0 0%,#a8907f 40%,#5b4437 70%,#2c1f19 100%)}
  .formula{position:absolute;left:640px;top:265px;width:230px;height:300px;background:var(--red);border-radius:22px;color:var(--white);
    display:flex;flex-direction:column;justify-content:center;align-items:center;text-align:center;font-family:"Roboto Condensed",Arial,sans-serif;font-size:21px;line-height:1.1;text-transform:uppercase}
  .formula .op{font-size:26px;font-weight:700;margin:6px 0}
</style>
</head>
<body>
<main class="spread">
  <section class="knowledge">
    <h1 class="knowledge__title">Oferecemos a você conhecimento <span>de mercado</span></h1>
    <ul class="insights">
      <li class="insight">
        <svg width="64" height="64" viewBox="0 0 64 64" aria-hidden="true"><circle cx="32" cy="32" r="31" fill="#fff"/><circle cx="32" cy="32" r="16" fill="#c4161c"/><path d="M32 32 L32 16 A16 16 0 0 1 48 32 Z" fill="#fff"/><path d="M34 30 L34 14 A16 16 0 0 1 50 30 Z" fill="#c4161c"/></svg>
        <p>Informações sobre o <b>consumo de vale-refeição</b> no estabelecimento.</p>
      </li>
      <li class="insight">
        <svg width="64" height="64" viewBox="0 0 64 64" aria-hidden="true"><circle cx="32" cy="32" r="31" fill="#fff"/><g fill="#c4161c"><circle cx="32" cy="20" r="5"/><path d="M24 32a8 6 0 0 1 16 0z"/><circle cx="20" cy="38" r="4"/><path d="M14 48a6 5 0 0 1 12 0z"/><circle cx="44" cy="38" r="4"/><path d="M38 48a6 5 0 0 1 12 0z"/></g><path d="M32 33v5M32 38l-12-3M32 38l12-3" stroke="#c4161c" stroke-width="1.5"/></svg>
        <p>Informações sobre o <b>perfil dos usuários</b> que frequentam o estabelecimento.</p>
      </li>
      <li class="insight">
        <svg width="64" height="64" viewBox="0 0 64 64" aria-hidden="true"><circle cx="32" cy="32" r="31" fill="#fff"/><path d="M16 28h32l-4 18H20z" fill="#c4161c"/><path d="M24 28l6-10M40 28l-6-10" stroke="#c4161c" stroke-width="2.5" stroke-linecap="round"/><path d="M26 32v10M32 32v10M38 32v10" stroke="#fff" stroke-width="2"/></svg>
        <p>Informações sobre preferências alimentares dos usuários.</p>
      </li>
    </ul>
    <p class="knowledge__note">O restaurante poderá ver essas informações com base no perfil de pessoas que consomem no próprio estabelecimento e na concorrência do bairro.</p>
  </section>

  <section class="lead"><h2>Esteja à <b>frente da concorrência!</b></h2></section>
  <div class="photo-service" role="img" aria-label="Foto de atendente servindo cliente em restaurante"></div>
  <section class="promise"><p>Ofereça sempre o que seu <b>cliente gosta e procura</b>, e prepare-se para ser <b>reconhecido</b> e <b>alavancar suas vendas!</b></p></section>

  <div class="photo-client" role="img" aria-label="Foto de cliente usando o celular e vitrine de doces no balcão"></div>
  <section class="formula">
    <span>Maior<br>conhecimento</span>
    <span class="op">+</span>
    <span>Melhor<br>atendimento</span>
    <span class="op">=</span>
    <span>Maior<br>fidelização</span>
  </section>
</main>
</body>
</html>
```